Copper Lantern Haulage

We are a 3PL freight brokerage company looking to create a website to attract new customers. Some ideas on how other freight websites look is located at these links, https://www.bluefinchcarriers.example/services, https://marlowcargo.example/freight-brokerage/.
We would like to have a quote feature implemented into this website.

We specialize in heavy-haul, specialized loads, flatbed, and dry vans.

```html
<!DOCTYPE html>
<html lang="en">
<head>
<meta charset="utf-8">
<title>Copper Lantern Haulage</title>
<link href="https://fonts.googleapis.com/css2?family=Raleway:wght@400;500;600;700&family=Nunito+Sans:wght@400;600;700&display=swap" rel="stylesheet">
<style>
:root{
  --navy:#1b365d;
  --navy-deep:#14294a;
  --nav:#2f5d87;
  --gold:#bf9530;
  --ink:#1f2a36;
  --muted:#4a525c;
  --line:#d9dde2;
  --soft:#f0f3f5;
  --white:#ffffff;
}
*{margin:0;padding:0;box-sizing:border-box}
html,body{width:1200px;height:3450px;overflow:hidden}
body{position:relative;background:var(--white);font-family:"Nunito Sans",Arial,sans-serif;color:var(--ink)}
.abs{position:absolute}
.btn{position:absolute;background:var(--gold);color:var(--white);font-size:11px;font-weight:700;letter-spacing:.3px;display:flex;align-items:center;justify-content:center;text-transform:uppercase}
/* header */
.brand{position:absolute;left:130px;top:34px;font-family:"Raleway",sans-serif;font-weight:700;font-size:19px;color:var(--navy);width:190px;line-height:1.2}
.contact-chip{position:absolute;top:36px;display:flex;align-items:center;gap:6px;font-size:13px;color:var(--ink);white-space:nowrap}
.chip-dot{width:26px;height:26px;border-radius:50%;background:var(--navy);display:flex;align-items:center;justify-content:center;flex:none}
.nav{position:absolute;left:0;top:97px;width:1200px;height:33px;background:var(--nav)}
.nav a{position:absolute;top:0;height:33px;line-height:33px;color:var(--white);font-size:11.5px;text-decoration:none;transform:translateX(-50%);white-space:nowrap}
.nav a.active{background:var(--gold);padding:0 14px}
/* hero */
.hero{position:absolute;left:0;top:130px;width:1200px;height:370px;background:linear-gradient(90deg,#0f2440 0%,#1a3352 55%,#13294a 100%)}
.hero-photo{position:absolute;left:710px;top:20px;width:360px;height:350px;background:linear-gradient(160deg,#6e7c72 0%,#c9a25c 55%,#3b3a36 100%)}
.hero-kicker{left:130px;top:106px;font-family:"Raleway",sans-serif;font-size:22px;color:var(--white)}
.hero-title{left:130px;top:130px;font-family:"Raleway",sans-serif;font-size:41px;font-weight:500;color:var(--white);white-space:nowrap}
.hero-sub{left:130px;top:190px;font-size:14px;color:var(--white)}
.slide-btn{position:absolute;top:331px;width:40px;height:39px;background:#e8e9eb;display:flex;align-items:center;justify-content:center}
/* modes */
.mode{position:absolute;top:570px;width:220px;height:220px;text-align:center}
.mode .icon{width:50px;height:44px;margin:0 auto;border-radius:6px}
.mode h3{font-family:"Raleway",sans-serif;font-weight:500;font-size:18px;margin-top:14px}
.mode p{font-size:12px;line-height:17px;margin:12px auto 0;width:190px;color:var(--muted)}
.mode.featured{background:var(--navy)}
.mode.featured h3,.mode.featured p{color:var(--white)}
.vline{position:absolute;width:1px;background:var(--line)}
/* sections */
.kicker{font-size:14px;color:var(--ink)}
.h2{font-family:"Raleway",sans-serif;font-weight:500;font-size:34px;color:var(--ink);white-space:nowrap}
.para{font-size:13px;line-height:19.5px;color:var(--ink)}
.hr{position:absolute;height:1px;background:var(--line)}
.services{position:absolute;left:0;top:1371px;width:1200px;height:495px;background:var(--soft)}
.svc{position:absolute;top:140px;width:220px;text-align:center}
.svc .photo{width:220px;height:217px;border-radius:22px 22px 0 0}
.svc h3{font-family:"Raleway",sans-serif;font-weight:500;font-size:18px;margin-top:17px}
.svc p{font-size:11.5px;line-height:17px;margin-top:10px;color:var(--muted)}
.testimonial{position:absolute;left:0;top:1866px;width:1200px;height:367px;background:linear-gradient(90deg,#3d4a45 0%,#2b3a36 40%,#1d2d33 70%,#233444 100%)}
.contact{position:absolute;left:0;top:2708px;width:1200px;height:350px;background:linear-gradient(135deg,#2a3038,#1c2229 60%,#252b31)}
.field{position:absolute;background:var(--white);font-size:10px;color:var(--ink);padding:10px 12px}
.footer{position:absolute;left:0;top:3058px;width:1200px;height:392px;background:var(--navy)}
.fcol h4{font-family:"Raleway",sans-serif;font-weight:500;font-size:17px;color:var(--gold);margin-bottom:14px}
.fcol li{list-style:none;font-size:12px;color:var(--white);line-height:26.8px}
.fcol li::before{content:"» ";color:var(--gold)}
.finfo{display:flex;align-items:flex-start;gap:10px;font-size:12px;color:var(--white);line-height:15px;margin-bottom:18px}
.ring{width:26px;height:26px;border:1.5px solid var(--gold);border-radius:50%;flex:none;display:flex;align-items:center;justify-content:center}
.social{position:absolute;width:34px;height:34px;border-radius:50%}
</style>
</head>
<body>

<header>
  <div class="brand">Copper Lantern Haulage</div>
  <div class="contact-chip" style="left:700px">
    <span class="chip-dot"><svg width="12" height="12" viewBox="0 0 24 24"><path fill="#fff" d="M6.6 10.8a15 15 0 006.6 6.6l2.2-2.2c.3-.3.7-.4 1-.2 1.1.4 2.3.6 3.6.6.6 0 1 .4 1 1V20c0 .6-.4 1-1 1A17 17 0 013 4c0-.6.4-1 1-1h3.5c.6 0 1 .4 1 1 0 1.3.2 2.5.6 3.6.1.3 0 .7-.2 1z"/></svg></span>
    +1 (555) 246 7030
  </div>
  <div class="contact-chip" style="left:852px;font-size:12.5px">
    <span class="chip-dot"><svg width="12" height="12" viewBox="0 0 24 24"><path fill="#fff" d="M3 5h18v14H3z"/><path d="M3 6l9 7 9-7" stroke="#1b365d" stroke-width="2" fill="none"/></svg></span>
    hello@copperlanternhaulage.example
  </div>
</header>

<nav class="nav">
  <a class="active" style="left:277px">HOME</a>
  <a style="left:370px">SERVICES</a>
  <a style="left:465px">ABOUT</a>
  <a style="left:561px">CARRIERS</a>
  <a style="left:672px">RESOURCES</a>
  <a style="left:787px">RACE TEAM</a>
  <a style="left:905px">GET A QUOTE</a>
</nav>

<section class="hero">
  <div class="hero-photo" role="img" aria-label="Semi truck on a forest road at sunset"></div>
  <div class="abs hero-kicker">Strongest</div>
  <div class="abs hero-title">Distribution Network</div>
  <div class="abs hero-sub">Heavy-haul, flatbed and dry-van freight, brokered right</div>
  <div class="btn" style="left:130px;top:224px;width:102px;height:34px">Read More</div>
  <div class="slide-btn" style="left:988px"><svg width="10" height="14"><path d="M8 1L2 7l6 6" stroke="#333" stroke-width="1.6" fill="none"/></svg></div>
  <div class="slide-btn" style="left:1032px"><svg width="10" height="14"><path d="M2 1l6 6-6 6" stroke="#333" stroke-width="1.6" fill="none"/></svg></div>
</section>

<div class="mode" style="left:130px;padding-top:50px">
  <div class="icon" role="img" aria-label="Heavy haul truck icon" style="background:#f2b33d"></div>
  <h3>Heavy Haul</h3>
  <p>Oversize machinery moved with permits and escorts</p>
</div>
<div class="vline" style="left:360px;top:610px;height:160px"></div>
<div class="mode" style="left:370px;padding-top:50px">
  <div class="icon" role="img" aria-label="Specialized load icon" style="background:#b9d3ea"></div>
  <h3>Specialized Loads</h3>
  <p>Custom plans for freight that needs extra care</p>
</div>
<div class="vline" style="left:600px;top:610px;height:160px"></div>
<div class="mode featured" style="left:610px;padding-top:30px">
  <div class="icon" role="img" aria-label="Flatbed trailer icon" style="background:#c8d4e3"></div>
  <h3>Flatbed</h3>
  <p>Open-deck capacity for steel, lumber and more</p>
  <div class="btn" style="left:59px;top:160px;width:101px;height:33px">Get a Quote</div>
</div>
<div class="vline" style="left:840px;top:610px;height:160px"></div>
<div class="mode" style="left:850px;padding-top:50px">
  <div class="icon" role="img" aria-label="Dry van trailer icon" style="background:#e9a84a"></div>
  <h3>Dry Van</h3>
  <p>Enclosed trailers for palletized general freight</p>
</div>

<div class="abs kicker" style="left:130px;top:963px">Welcome To</div>
<div class="abs h2" style="left:130px;top:980px">Copper Lantern Haulage</div>
<p class="abs para" style="left:130px;top:1046px;width:400px">But I must explain to you how all this mistaken idea of denouncing pleasure and praising pain was born and I will give you a complete account of the system, and expound the actual teachings of the great explorer of the truth.</p>
<div class="hr" style="left:130px;top:1138px;width:460px"></div>
<div class="vline" style="left:590px;top:922px;height:338px"></div>
<div class="btn" style="left:130px;top:1155px;width:102px;height:34px">Read More</div>
<div class="abs" style="left:680px;top:1025px;width:280px;height:276px;background:var(--gold);border-radius:0 0 0 70px"></div>
<div class="abs" style="left:692px;top:880px;width:378px;height:411px;background:linear-gradient(160deg,#1b3a3a,#3d4b44 55%,#5a4a36);border-radius:0 60px 0 60px" role="img" aria-label="Truck on a road at dusk"></div>

<section class="services">
  <div class="abs h2" style="left:0;width:1200px;text-align:center;top:52px">Our Services</div>
  <div class="abs" style="left:0;width:1200px;text-align:center;top:97px;font-size:13px">Sed ut perspiciatis unde omnis iste natus error sit voluptatem</div>
  <div class="svc" style="left:130px"><div class="photo" role="img" aria-label="Warehouse worker reviewing paperwork" style="background:linear-gradient(160deg,#6b7a86,#2f6fae)"></div><h3>Transparent Pricing</h3><p>Lorem ipsum dolor sit amet, consectetur adipiscing elit.</p></div>
  <div class="svc" style="left:370px"><div class="photo" role="img" aria-label="Tall warehouse shelving with boxes" style="background:linear-gradient(160deg,#8a7356,#3a3128)"></div><h3>Warehouse Storage</h3><p>Lorem ipsum dolor sit amet, consectetur adipiscing elit.</p></div>
  <div class="svc" style="left:610px"><div class="photo" role="img" aria-label="Trucks on a road with tracking overlay" style="background:linear-gradient(160deg,#aab6c6,#5e6f88)"></div><h3>Real-Time Tracking</h3><p>Lorem ipsum dolor sit amet, consectetur adipiscing elit.</p></div>
  <div class="svc" style="left:850px"><div class="photo" role="img" aria-label="Loading dock doors in a warehouse" style="background:linear-gradient(180deg,#6f8d9a,#c7c9cb)"></div><h3>Security for Cargo</h3><p>Lorem ipsum dolor sit amet, consectetur adipiscing elit.</p></div>
</section>

<section class="testimonial" role="img" aria-label="Truck driving along a forest highway">
  <svg class="abs" style="left:633px;top:52px" width="46" height="34"><path d="M2 32V14C2 6 8 2 16 2M24 32V14c0-8 6-12 14-12M2 18h18v14H2M24 18h18v14H24" stroke="#fff" stroke-width="1.5" fill="none" opacity=".8"/></svg>
  <div class="abs" style="left:632px;top:110px;width:470px;font-family:'Raleway',sans-serif;font-size:24px;line-height:37px;color:var(--white);letter-spacing:.3px">Enim ad minima veniam, quis nostrum exercitationem ullam corporis suscipit laboriosam.</div>
  <div class="abs" style="left:633px;top:259px;width:60px;height:60px;border-radius:50%;background:#c7ccd1;border:2px solid #fff" role="img" aria-label="Client portrait"></div>
  <div class="abs" style="left:705px;top:268px;font-size:14px;color:var(--white)">Satisfied Client</div>
  <div class="abs" style="left:705px;top:286px;font-family:'Raleway',sans-serif;font-size:23px;color:var(--white)">Harlan Beech</div>
</section>

<div class="abs kicker" style="left:130px;top:2343px">Fast and Reliable</div>
<div class="abs h2" style="left:130px;top:2360px">Shipping Services</div>
<p class="abs para" style="left:130px;top:2426px;width:400px">But I must explain to you how all this mistaken idea of denouncing pleasure and praising pain was born and I will give you a complete account of the system...</p>
<div class="hr" style="left:130px;top:2507px;width:460px"></div>
<div class="vline" style="left:590px;top:2303px;height:337px"></div>
<div class="btn" style="left:130px;top:2534px;width:102px;height:34px">Read More</div>
<div class="abs" style="left:610px;top:2303px;width:460px;height:336px;background:linear-gradient(180deg,#9fb0bd 0%,#9aabb8 50%,#3e6a7e 62%,#2b5568 100%)" role="img" aria-label="Container ship at sea"></div>

<section class="contact" role="img" aria-label="Aerial view of a container yard">
  <div class="abs" style="left:0;width:1200px;text-align:center;top:62px;font-size:13px;color:var(--white)">Get a Quote</div>
  <div class="abs" style="left:0;width:1200px;text-align:center;top:78px;font-family:'Raleway',sans-serif;font-size:34px;color:var(--white)">Request Your Freight Quote</div>
  <div class="abs" style="left:0;width:1200px;text-align:center;top:126px;font-size:13px;color:var(--white)">Tell us about your load and we will send a rate within one business day</div>
  <div class="field" style="left:320px;top:170px;width:277px;height:33px">Name:</div>
  <div class="field" style="left:320px;top:210px;width:277px;height:33px">Email:</div>
  <div class="field" style="left:320px;top:250px;width:277px;height:33px">Phone:</div>
  <div class="field" style="left:604px;top:170px;width:276px;height:73px">Load details:</div>
  <div class="btn" style="left:604px;top:250px;width:276px;height:33px;font-size:10px">Get Quote</div>
</section>

<footer class="footer">
  <svg class="abs" style="left:0;top:0" width="1200" height="392"><polygon points="0,250 0,392 130,392" fill="#e9edf2"/><polygon points="0,170 170,40 320,40 360,392 170,392 0,230" fill="#1e3b66" opacity=".7"/></svg>
  <div class="abs" style="left:130px;top:125px;width:230px;font-family:'Raleway',sans-serif;font-weight:700;font-size:24px;line-height:28px;color:var(--white)">Copper Lantern Haulage</div>
  <div class="social" style="left:131px;top:201px;background:#1f6ff2"></div>
  <div class="social" style="left:185px;top:201px;background:var(--gold)"></div>
  <div class="social" style="left:239px;top:201px;background:var(--gold)"></div>

  <div class="abs fcol" style="left:436px;top:45px;width:270px">
    <h4>Contact Us</h4>
    <div class="finfo"><span class="ring"><svg width="10" height="12" viewBox="0 0 10 12"><path d="M5 11S1 7 1 4.5a4 4 0 018 0C9 7 5 11 5 11z" stroke="#bf9530" fill="none"/></svg></span><span style="padding-top:3px">4120 Lantern Row Suite,<br>BX210k</span></div>
    <div class="finfo"><span class="ring"><svg width="10" height="10" viewBox="0 0 24 24"><path fill="#bf9530" d="M6.6 10.8a15 15 0 006.6 6.6l2.2-2.2c.3-.3.7-.4 1-.2 1.1.4 2.3.6 3.6.6.6 0 1 .4 1 1V20c0 .6-.4 1-1 1A17 17 0 013 4c0-.6.4-1 1-1h3.5c.6 0 1 .4 1 1 0 1.3.2 2.5.6 3.6.1.3 0 .7-.2 1z"/></svg></span><span style="padding-top:6px">555.318.4420</span></div>
    <div class="finfo"><span class="ring"><svg width="11" height="8"><rect x=".5" y=".5" width="10" height="7" stroke="#bf9530" fill="none"/><path d="M.5 .5l5 4 5-4" stroke="#bf9530" fill="none"/></svg></span><span style="padding-top:6px;font-size:11px">office@copperlanternhaulage.example</span></div>
  </div>
  <div class="abs fcol" style="left:731px;top:45px">
    <h4>Quick Links</h4>
    <ul><li>Home</li><li>Services</li><li>About Us</li><li>Carriers</li><li>Resources</li><li>Race Team</li><li>Get a Quote</li></ul>
  </div>
  <div class="abs fcol" style="left:931px;top:45px">
    <h4>Services</h4>
    <ul><li>Heavy Haul</li><li>Specialized Loads</li><li>Flatbed</li><li>Dry Van</li><li>Security for CargoSafe</li></ul>
  </div>
  <div class="hr" style="left:130px;top:310px;width:940px;background:#34507a"></div>
  <div class="abs" style="left:0;width:1200px;text-align:center;top:335px;font-size:11px;color:var(--white)">© 2022 <span style="color:var(--gold)">Copper Lantern Haulage</span>. All Rights Reserved.</div>
</footer>

</body>
</html>
```